Contemporary Media Company with Logo Needs Business Card Design

Need a modern card design for a full service digital media company using the logo included. Also want the info below on the card. Probably list the services on the card back to save space for the front. Want something contemporary to impress prospective clients. You may want to submit both a somewhat more conservative design, and then a more wild one.
General Info: (this phrase need not be on the card)
Ned Parlow
Founder and CEO
949-612-4830
ned@vontaramedia.example
vontaramedia.example
Services: (this word need not be on the card)
Content & Experience Strategy
Brand Development
Search Engine Optimization
Website Design
Website Operation
Social Media Integration
Complete Video Solutions
Updates
Industry/Entity Type
Business
Contact Information for Business Card
Ned Parlow
Founder and CEO
949-612-4830
ned@vontaramedia.example
vontaramedia.example
Brand Development
Website Design
Website Operation
Social Media Integration
Complete Video Solutions
Look and feel
Each slider illustrates characteristics of the customer's brand and the style your logo design should communicate.

```html
<!DOCTYPE html>
<html lang="en">
<head>
<meta charset="utf-8">
<title>Vontara Media – Business Card</title>
<link rel="stylesheet" href="https://fonts.googleapis.com/css2?family=Open+Sans:wght@400;600;700&display=swap">
<style>
  :root {
    --backdrop: #e8e5e1;
    --ink-black: #0b0b0b;
    --paper-white: #ffffff;
    --brand-orange: #f0892a;
    --brand-grey: #6f6f6f;
    --grey-band: #555555;
    --text-dark: #444444;
    --text-light: #ffffff;
  }
  * { box-sizing: border-box; margin: 0; padding: 0; }
  html, body {
    width: 1200px; height: 913px; overflow: hidden;
    background: var(--backdrop);
    font-family: "Open Sans", Arial, sans-serif;
  }
  .canvas { position: relative; width: 1200px; height: 913px; }
  .card {
    position: absolute; width: 560px; height: 320px; overflow: hidden;
    border-radius: 3px; box-shadow: 0 10px 24px rgba(0,0,0,.22);
  }
  .card--front { left: 80px; top: 110px; background: var(--ink-black); }
  .card--back  { left: 580px; top: 480px; background: var(--paper-white); }

  .brand { position: absolute; display: flex; align-items: center; gap: 16px; }
  .brand__square { width: 44px; height: 44px; background: var(--brand-orange); }
  .brand__name {
    font-weight: 400; font-size: 34px; letter-spacing: 3px; text-transform: uppercase;
  }
  .card--front .brand { left: 40px; top: 56px; }
  .card--front .brand__name { color: var(--text-light); }
  .card--back .brand { left: 40px; top: 34px; }
  .card--back .brand__square { width: 58px; height: 58px; }
  .card--back .brand__name { color: var(--brand-grey); }

  .contact {
    position: absolute; right: 28px; top: 128px; list-style: none;
    color: var(--text-light); font-size: 13px; line-height: 21px; text-align: right;
  }
  .contact li { display: flex; justify-content: flex-end; align-items: center; gap: 7px; }
  .contact svg { width: 12px; height: 12px; fill: none; stroke: var(--brand-orange); stroke-width: 2; }

  .person { position: absolute; left: 40px; top: 168px; }
  .person__name { color: var(--text-light); font-weight: 700; font-size: 22px; line-height: 26px; }
  .person__title { color: var(--brand-orange); font-weight: 400; font-size: 15px; }

  .divider { position: absolute; left: 28px; right: 22px; top: 222px; height: 1px; background: var(--text-light); }
  .band { position: absolute; }
  .band--orange-front { left: 330px; right: 0; top: 234px; height: 26px; background: var(--brand-orange); }
  .band--white-front { left: 0; width: 330px; top: 264px; height: 28px; background: var(--paper-white); }
  .band--orange-back { left: 340px; right: 0; top: 150px; height: 28px; background: var(--brand-orange); }
  .band--grey-back { left: 0; right: 0; top: 270px; height: 26px; background: var(--grey-band); }

  .services {
    position: absolute; left: 40px; top: 116px; list-style: none;
    color: var(--text-dark); font-size: 14px; font-weight: 600; line-height: 20px;
  }
  .services li { display: flex; align-items: center; gap: 8px; }
  .services li::before { content: ""; width: 7px; height: 7px; background: var(--brand-orange); }
</style>
</head>
<body>
<main class="canvas">
  <section class="card card--front" aria-label="Business card front">
    <div class="brand">
      <span class="brand__square"></span>
      <span class="brand__name">Vontara Media</span>
    </div>
    <ul class="contact">
      <li>949-612-4830
        <svg viewBox="0 0 12 12"><path d="M2 1.5l2 0 1 2.5-1.3 1a6 6 0 0 0 3.3 3.3l1-1.3 2.5 1v2a1 1 0 0 1-1 1A9 9 0 0 1 1 2.5a1 1 0 0 1 1-1z"/></svg></li>
      <li>ned@vontaramedia.example
        <svg viewBox="0 0 12 12"><rect x="1" y="2.5" width="10" height="7"/><path d="M1 2.5l5 4 5-4"/></svg></li>
      <li>www.vontaramedia.example
        <svg viewBox="0 0 12 12"><circle cx="6" cy="6" r="5"/><path d="M1 6h10M6 1c-2.5 3-2.5 7 0 10M6 1c2.5 3 2.5 7 0 10"/></svg></li>
    </ul>
    <div class="person">
      <p class="person__name">Ned Parlow</p>
      <p class="person__title">Founder and CEO</p>
    </div>
    <div class="divider"></div>
    <div class="band band--orange-front"></div>
    <div class="band band--white-front"></div>
  </section>

  <section class="card card--back" aria-label="Business card back">
    <div class="brand">
      <span class="brand__square"></span>
      <span class="brand__name">Vontara Media</span>
    </div>
    <div class="band band--orange-back"></div>
    <ul class="services">
      <li>Content &amp; Experience Strategy</li>
      <li>Brand Development</li>
      <li>Search Engine Optimization</li>
      <li>Website Design</li>
      <li>Website Operation</li>
      <li>Social Media Integration</li>
      <li>Complete Video Solutions</li>
    </ul>
    <div class="band band--grey-back"></div>
  </section>
</main>
</body>
</html>
```